Design a BOLD Ad Design for Fitness Club

We are fitness facility that is about to run our new "Bright Parent Reboot" program and we need a bold design created for an ad that will run on Instagram and Facebook.

The ad needs to be eye catching, easy to read and attractive so that someone stops scrolling and clicks to join.

The add needs to be sized to 1080 x 1080, include our logo and the text "Bright Parent Reboot" and "Starting September 23rd"

I have included an example photo, which is to be used as an example only of a design style that stands out to us, (colors, female photo style, etc)

I have also included our logo, which the yellow color can be changed for this design.

Thank you and we look forward to seeing your design.

```html
<!DOCTYPE html>
<html lang="en">
<head>
<meta charset="utf-8">
<title>Bright Parent Reboot – Ad</title>
<link href="https://fonts.googleapis.com/css2?family=Anton&family=Oswald:wght@700&family=Montserrat:wght@800&family=Yellowtail&display=swap" rel="stylesheet">
<style>
  :root{
    --purple:#aa0e80;
    --purple-deep:#7e0860;
    --magenta:#d6098a;
    --yellow:#f7d000;
    --ink:#1c1c1c;
    --white:#ffffff;
  }
  html,body{margin:0;padding:0;overflow:hidden;background:var(--white);}
  .ad{position:relative;width:1200px;height:1200px;overflow:hidden;background:var(--purple);}
  .ad svg{position:absolute;inset:0;width:1200px;height:1200px;display:block;}
  .headline{font-family:"Anton",sans-serif;}
  .headline-shadow{fill:var(--purple-deep);}
  .headline-main{fill:var(--white);}
  .script{font-family:"Yellowtail",cursive;fill:var(--yellow);stroke:var(--purple);stroke-width:10px;paint-order:stroke;stroke-linejoin:round;}
  .date-text{font-family:"Oswald",sans-serif;font-weight:700;fill:var(--white);}
  .brand-name{font-family:"Oswald",sans-serif;font-weight:700;fill:var(--white);}
  .brand-tag{font-family:"Montserrat",sans-serif;font-weight:800;fill:var(--ink);letter-spacing:5px;}
</style>
</head>
<body>
<div class="ad">
  <svg viewBox="0 0 1200 1200" xmlns="http://www.w3.org/2000/svg">
    <defs>
      <linearGradient id="modelTone" x1="0" y1="0" x2="0" y2="1">
        <stop offset="0" stop-color="#6b4330"/>
        <stop offset="0.4" stop-color="#c98a63"/>
        <stop offset="0.75" stop-color="#e0242b"/>
        <stop offset="1" stop-color="#c98a63"/>
      </linearGradient>
      <linearGradient id="dotTone" x1="0" y1="0" x2="1" y2="1">
        <stop offset="0" stop-color="#c2108a" stop-opacity="0"/>
        <stop offset="1" stop-color="#c2108a" stop-opacity="0.35"/>
      </linearGradient>
    </defs>

    <!-- background accents -->
    <polygon class="accent-triangle" points="0,0 129,0 244,308 0,131" fill="var(--magenta)"/>
    <rect class="dot-field" x="910" y="0" width="290" height="360" fill="url(#dotTone)"/>

    <!-- yellow lower band -->
    <path class="yellow-band" d="M0,731 C220,800 430,930 640,950 C860,960 1040,850 1200,777 L1200,1200 L0,1200 Z" fill="var(--yellow)"/>

    <!-- model photo area -->
    <rect class="model-photo" role="img" aria-label="Photo: smiling woman in a red sports top flexing her arm"
      x="700" y="520" width="500" height="680" rx="40" fill="url(#modelTone)" opacity="0.9"/>

    <!-- headline -->
    <g class="headline" font-size="250">
      <g transform="translate(291 334) rotate(-8) skewX(-8)">
        <text class="headline-shadow" x="7" y="7" textLength="546" lengthAdjust="spacingAndGlyphs">BRIGHT</text>
        <text class="headline-main" x="0" y="0" textLength="546" lengthAdjust="spacingAndGlyphs">BRIGHT</text>
      </g>
      <g transform="translate(162 602) rotate(-8) skewX(-8)">
        <text class="headline-shadow" x="7" y="7" textLength="860" lengthAdjust="spacingAndGlyphs">PARENT</text>
        <text class="headline-main" x="0" y="0" textLength="860" lengthAdjust="spacingAndGlyphs">PARENT</text>
      </g>
    </g>
    <text class="script" x="0" y="0" font-size="130" text-anchor="middle" textLength="380" lengthAdjust="spacingAndGlyphs" transform="translate(440 610) rotate(-18)">Reboot</text>

    <!-- start date badge -->
    <circle class="date-badge" cx="234" cy="828" r="153" fill="var(--ink)"/>
    <g class="date-text" text-anchor="middle">
      <text x="234" y="792" font-size="46">STARTING</text>
      <text x="234" y="846" font-size="46">SEPTEMBER</text>
      <text x="234" y="900" font-size="46">23RD</text>
    </g>

    <!-- brand -->
    <rect class="brand-mark" x="72" y="1040" width="40" height="40" fill="var(--white)"/>
    <text class="brand-name" x="126" y="1106" font-size="130" textLength="460" lengthAdjust="spacingAndGlyphs">PULSEFORGE</text>
    <text class="brand-tag" x="329" y="1144" font-size="18" text-anchor="middle">PERSONAL GROUP TRAINING</text>
  </svg>
</div>
</body>
</html>
```